Pathways to Brightmoor Land Ventures

size of the ad - 8”x 10.75" plus 0.25" bleed
I would like an ad for a magazine that will stand out and make people want to read the ad.
The ad should not be crowded and people reading the ad will be able to read the text.
I would like it to be a creative and modern-day design.
the list of topics should not be the focus of the ad.
the text is attached.
If you decide to use people in the ad then please no ladies.
please note that leave over 1 inch for the bottom of the footer

```html
<!DOCTYPE html>
<html lang="en">
<head>
<meta charset="utf-8">
<title>Real Estate Course</title>
<link rel="stylesheet" href="https://fonts.googleapis.com/css2?family=Nunito+Sans:ital,wght@0,400;0,600;0,700;0,800;0,900;1,800&display=swap">
<style>
  :root {
    --navy: #1a4070;
    --teal: #5ec4c1;
    --white: #ffffff;
    --sky-light: #8a96b6;
    --sky-dark: #2b3f6b;
  }
  * { margin: 0; padding: 0; box-sizing: border-box; }
  html, body { width: 893px; height: 1200px; overflow: hidden; background: var(--white); }
  body { font-family: "Nunito Sans", Arial, sans-serif; }
  .ad { position: relative; width: 893px; height: 1200px; overflow: hidden; background: var(--white); }

  .quote-mark { position: absolute; left: 56px; top: 68px; width: 48px; height: 48px; border-radius: 50%; background: var(--teal); }
  .quote {
    position: absolute; left: 118px; top: 68px;
    font-size: 24px; line-height: 30px; font-weight: 800; font-style: italic;
    color: var(--navy);
  }

  .hero-band { position: absolute; left: 0; top: 207px; width: 893px; height: 480px; background: var(--navy); }

  .skyline-photo {
    position: absolute; left: 0; top: 687px; width: 893px; height: 513px;
    background: linear-gradient(160deg, var(--sky-light) 0%, #6c7aa0 40%, #4b5d88 70%, var(--sky-dark) 100%);
  }

  .title {
    position: absolute; left: 54px; top: 250px;
    font-weight: 700; font-size: 81px; line-height: 80px; letter-spacing: -1px;
    color: var(--teal);
  }
  .title .accent { color: var(--white); }

  .intro {
    position: absolute; left: 56px; top: 513px; width: 420px;
    font-size: 23.5px; line-height: 28px; font-weight: 400; color: var(--white);
  }

  .topics {
    position: absolute; left: 581px; top: 0; width: 256px; height: 836px;
    background: var(--teal); color: var(--white);
  }
  .topics-heading {
    position: absolute; left: 27px; top: 126px;
    font-size: 31px; line-height: 35px; font-weight: 600;
  }
  .topics-rule {
    position: absolute; left: 28px; top: 219px; width: 202px; height: 4px;
    background: radial-gradient(circle, var(--white) 1.7px, transparent 2px) 0 0 / 8.4px 4px repeat-x;
  }
  .topic {
    position: absolute; left: 72px; width: 180px;
    font-size: 20.5px; line-height: 24.5px; font-weight: 400;
  }
  .topic-icon { position: absolute; left: -42px; width: 26px; height: 36px; }

  .sessions {
    position: absolute; left: 61px; top: 957px; width: 320px; height: 186px;
    background: var(--teal); color: var(--navy);
    padding: 24px 0 0 18px;
  }
  .sessions-date { font-size: 29px; line-height: 30px; font-weight: 800; letter-spacing: -0.3px; }
  .sessions-place { font-size: 23px; line-height: 26px; font-weight: 700; margin-top: 6px; }
  .sessions-detail { font-size: 17.5px; line-height: 22px; font-weight: 600; }

  .offer-badge { position: absolute; left: 617px; top: 933px; width: 210px; height: 210px; }
  .offer-text {
    position: absolute; left: 617px; top: 983px; width: 210px; text-align: center;
    font-size: 32px; line-height: 32px; font-weight: 900; color: var(--navy);
  }
</style>
</head>
<body>
<div class="ad">
  <svg width="0" height="0" style="position:absolute">
    <defs>
      <symbol id="building" viewBox="0 0 26 36">
        <path d="M1 36V8h6V3h3V0h2v3h3v5h4v4h6v24z" fill="#1a4070"/>
        <g fill="#5ec4c1">
          <rect x="3" y="11" width="2" height="3"/><rect x="7" y="11" width="2" height="3"/><rect x="11" y="11" width="2" height="3"/><rect x="15" y="11" width="2" height="3"/>
          <rect x="3" y="17" width="2" height="3"/><rect x="7" y="17" width="2" height="3"/><rect x="11" y="17" width="2" height="3"/><rect x="15" y="17" width="2" height="3"/><rect x="20" y="17" width="2" height="3"/>
          <rect x="3" y="23" width="2" height="3"/><rect x="7" y="23" width="2" height="3"/><rect x="11" y="23" width="2" height="3"/><rect x="15" y="23" width="2" height="3"/><rect x="20" y="23" width="2" height="3"/>
          <rect x="3" y="29" width="2" height="3"/><rect x="7" y="29" width="2" height="3"/><rect x="11" y="29" width="2" height="3"/><rect x="15" y="29" width="2" height="3"/><rect x="20" y="29" width="2" height="3"/>
        </g>
      </symbol>
    </defs>
  </svg>

  <div class="quote-mark"></div>
  <p class="quote">“Investing in knowledge is<br>investing in opportunities”</p>

  <div class="hero-band"></div>
  <div class="skyline-photo" role="img" aria-label="Upward view of glass office towers against a cloudy sky"></div>

  <h1 class="title">REAL<br>ESTATE<br><span class="accent">COURSE</span></h1>
  <p class="intro">Suitable for those that started or would like to go into real estate, this course will explore the foundations of commercial real estate.</p>

  <aside class="topics">
    <h2 class="topics-heading">Topics<br>Partial Listing</h2>
    <div class="topics-rule"></div>
    <div class="topic" style="top:254px"><svg class="topic-icon" style="top:2px"><use href="#building"/></svg>Real estate investment strategies</div>
    <div class="topic" style="top:346px"><svg class="topic-icon" style="top:-8px"><use href="#building"/></svg>Due diligence</div>
    <div class="topic" style="top:390px"><svg class="topic-icon" style="top:-7px"><use href="#building"/></svg>Financing</div>
    <div class="topic" style="top:434px"><svg class="topic-icon" style="top:-7px"><use href="#building"/></svg>Underwriting</div>
    <div class="topic" style="top:477px"><svg class="topic-icon" style="top:7px"><use href="#building"/></svg>Property management</div>
    <div class="topic" style="top:546px"><svg class="topic-icon" style="top:4px"><use href="#building"/></svg>Real estate legal basics</div>
    <div class="topic" style="top:614px"><svg class="topic-icon" style="top:-6px"><use href="#building"/></svg>Sourcing deals</div>
    <div class="topic" style="top:658px"><svg class="topic-icon" style="top:-7px"><use href="#building"/></svg>Syndication</div>
    <div class="topic" style="top:702px"><svg class="topic-icon" style="top:2px"><use href="#building"/></svg>Dealing with brokers</div>
    <div class="topic" style="top:770px"><svg class="topic-icon" style="top:-12px"><use href="#building"/></svg>Tax fundamentals</div>
  </aside>

  <section class="sessions">
    <p class="sessions-date">SESSIONS STARTING<br>28 FEBRUARY 2023</p>
    <p class="sessions-place">Harrow Glen</p>
    <p class="sessions-detail">10 - Tuesday evenings sessions<br>Limited Partial Scholarships</p>
  </section>

  <svg class="offer-badge" viewBox="-105 -105 210 210" aria-hidden="true">
    <polygon fill="#ffffff" points="100,0 82.7,14.6 94,34.2 72.7,42 76.6,64.3 54,64.3 50,86.6 28.7,78.9 17.4,98.5 0,84 -17.4,98.5 -28.7,78.9 -50,86.6 -54,64.3 -76.6,64.3 -72.7,42 -94,34.2 -82.7,14.6 -100,0 -82.7,-14.6 -94,-34.2 -72.7,-42 -76.6,-64.3 -54,-64.3 -50,-86.6 -28.7,-78.9 -17.4,-98.5 0,-84 17.4,-98.5 28.7,-78.9 50,-86.6 54,-64.3 76.6,-64.3 72.7,-42 94,-34.2 82.7,-14.6"/>
  </svg>
  <p class="offer-text">EARLY<br>BIRD<br>OFFER!</p>
</div>
</body>
</html>
```